Wine Label for a White and a Red Wine from Italy

We have a very good idea of what we want with artwork. We need you to please design a 'template' with the text so we can change out the artwork from year to year. Samples are shown of what we are looking for. We are looking for options with the two basic designs. Brand name of wine is: Valora di Castegno. Both wines are in a light green Bordeaux-style bottle (note: we don't show a light green bottle in the mockup but please remember the bottle is light green). Artwork is provided. We'd like to see either the green or blue butterfly on the white wine, the red butterfly is for the red wine. Please base the design on the attached label from Brailey and/or the attached label from Chateau Mervanges.

Target Market(s)

Millennials, women

Requirements
Must have
• The artwork (butterflies) attached.
Nice to have
• Elegant, readable fonts. Please make the text so it can be changed by the printer. Please make it so the artwork can be changed too.

```html
<!DOCTYPE html>
<html lang="en">
<head>
<meta charset="utf-8">
<title>Valora di Castegno – Barrel Select Labels</title>
<link href="https://fonts.googleapis.com/css2?family=Nunito+Sans:wght@200;300;400;800;900&display=swap" rel="stylesheet">
<style>
  :root {
    --backdrop: #ececec;
    --paper: #fbfcfb;
    --blanco-ink: #5f7c4b;
    --rosso-ink: #7b2416;
    --butterfly-green: #6f8f4a;
    --butterfly-cream: #ede8da;
    --splash-gold: #f2a81e;
    --splash-amber: #e8901a;
    --butterfly-red: #b8391f;
  }
  * { box-sizing: border-box; margin: 0; padding: 0; }
  html, body {
    width: 1200px; height: 1200px; overflow: hidden;
    background: var(--backdrop);
    font-family: "Nunito Sans", sans-serif;
  }
  .label-pair {
    width: 1200px; height: 1200px;
    display: flex; justify-content: center; align-items: center; gap: 120px;
  }
  .label {
    position: relative;
    width: 460px; height: 860px;
    background: var(--paper);
    overflow: hidden;
    box-shadow: 0 6px 24px rgba(0,0,0,0.12);
  }
  .label--blanco { color: var(--blanco-ink); }
  .label--rosso { color: var(--rosso-ink); }

  .artwork { position: absolute; z-index: 0; }
  .artwork--blanco {
    left: 40px; top: 300px; width: 400px; height: 380px;
    background: radial-gradient(ellipse at 50% 45%, var(--butterfly-green) 0%, #9bb27a 35%, var(--butterfly-cream) 65%, rgba(251,252,251,0) 80%);
  }
  .artwork--rosso {
    left: 20px; top: 90px; width: 440px; height: 680px;
    background:
      radial-gradient(ellipse at 50% 48%, var(--butterfly-red) 0%, #c8502a 20%, rgba(232,144,26,0) 42%),
      radial-gradient(ellipse at 55% 50%, var(--splash-gold) 0%, var(--splash-amber) 45%, rgba(251,252,251,0) 75%);
  }

  .label-text { position: relative; z-index: 1; text-align: center; }
  .brand-name {
    position: absolute; top: 46px; left: 0; right: 0;
    font-weight: 200; font-size: 50px; line-height: 1.05; letter-spacing: 1px;
    text-transform: uppercase;
  }
  .range {
    position: absolute; top: 168px; left: 0; right: 0;
    font-weight: 800; font-size: 26px; letter-spacing: 1px;
  }
  .vintage {
    position: absolute; top: 198px; left: 0; right: 0;
    font-weight: 900; font-size: 76px; letter-spacing: -2px; line-height: 1;
  }
  .wine-name {
    position: absolute; top: 692px; left: 0; right: 0;
    font-weight: 900; font-size: 50px; line-height: 1;
  }
  .origin {
    position: absolute; top: 742px; left: 0; right: 0;
    font-weight: 300; font-size: 26px; letter-spacing: -0.5px;
  }
  .producer {
    position: absolute; top: 786px; left: 0; right: 0;
    font-weight: 400; font-size: 17px; line-height: 1.3;
  }
</style>
</head>
<body>
  <main class="label-pair">
    <section class="label label--blanco">
      <div class="artwork artwork--blanco" role="img" aria-label="Painted green butterfly artwork, brushstroke style"></div>
      <div class="label-text">
        <h1 class="brand-name">Valora di<br>Castegno</h1>
        <p class="range">BARREL SELECT</p>
        <p class="vintage">2018</p>
        <h2 class="wine-name">BLANCO</h2>
        <p class="origin">PIEMONTE, ITALY</p>
        <p class="producer">Artisanlly Crafted by Cantina Sette Colli<br>Sustainably farmed</p>
      </div>
    </section>

    <section class="label label--rosso">
      <div class="artwork artwork--rosso" role="img" aria-label="Painted red butterfly on a golden orange brushstroke splash"></div>
      <div class="label-text">
        <h1 class="brand-name">Valora di<br>Castegno</h1>
        <p class="range">BARREL SELECT</p>
        <p class="vintage">2018</p>
        <h2 class="wine-name">ROSSO</h2>
        <p class="origin">PIEMONTE, ITALY</p>
        <p class="producer">Artisanlly Crafted by Cantina Sette Colli<br>Sustainably farmed</p>
      </div>
    </section>
  </main>
</body>
</html>
```